Life Coaching Business Card

Please check out my website at www.lorettavanmeer.example. Ideally I would like to use the same colors that I used on the site to match my business cards i.e: pink, green, teal, white
I want the final design to include a picture of me and also to be appealing and eye catching. For the picture I submitted, you can crop it smaller to just have my face (exclude my chest) showing.
Industry/Entity Type
Business
Contact Information for Business Card
Loretta Vanmeer
Transformational Life Coach
web: www.lorettavanmeer.example
email: loretta@lorettavanmeer.example
Phone: 555-318-4072
Look and feel
Each slider illustrates characteristics of the customer's brand and the style your logo design should communicate.

```html
<!DOCTYPE html>
<html lang="en">
<head>
<meta charset="utf-8">
<title>Loretta Vanmeer – Business Card</title>
<link rel="stylesheet" href="https://fonts.googleapis.com/css2?family=Josefin+Slab:wght@400;600;700&family=Open+Sans:wght@400&display=swap">
<style>
  :root {
    --bg: #e8e5e0;
    --teal: #5fb3c4;
    --teal-deep: #3f8fa1;
    --pink: #e6248f;
    --green: #c9dc34;
    --ink: #1d1d1d;
    --panel: rgba(236, 236, 236, 0.9);
    --photo-dark: #3a3a3a;
    --photo-light: #c9c9c9;
  }
  * { margin: 0; padding: 0; box-sizing: border-box; }
  html, body { width: 1200px; height: 900px; overflow: hidden; }
  body { background: var(--bg); position: relative; font-family: "Open Sans", sans-serif; }

  .card {
    position: absolute;
    width: 680px;
    height: 388px;
    overflow: hidden;
    box-shadow: 0 10px 26px rgba(0,0,0,0.18);
  }

  /* Back of card */
  .card--back { left: 300px; top: 40px; }
  .back-photo {
    position: absolute; inset: 0;
    background: linear-gradient(135deg, var(--teal-deep) 0%, var(--teal) 55%, #8fcfdb 100%);
  }
  .title-band {
    position: absolute; left: 0; right: 0; top: 120px; height: 200px;
    background: rgba(238, 240, 240, 0.88);
    border-top: 5px solid var(--pink);
  }
  .title-band__kicker {
    position: absolute; left: 40px; top: 34px;
    font-family: "Josefin Slab", serif; font-weight: 600;
    font-size: 22px; line-height: 1; color: var(--ink); letter-spacing: 0.5px;
  }
  .title-band__headline {
    position: absolute; left: 36px; top: 62px;
    font-family: "Josefin Slab", serif; font-weight: 600;
    font-size: 100px; line-height: 1; color: var(--ink); letter-spacing: 2px;
    white-space: nowrap;
  }
  .tagline-band {
    position: absolute; left: 0; right: 0; bottom: 0; height: 40px;
    background: var(--green);
    display: flex; align-items: center; justify-content: flex-end; padding-right: 34px;
    font-family: "Josefin Slab", serif; font-weight: 700;
    font-size: 22px; color: var(--ink);
  }

  /* Front of card */
  .card--front { left: 220px; top: 470px; background: var(--photo-light); }
  .front-photo {
    position: absolute; left: 0; top: 0; bottom: 0; width: 290px;
    background: linear-gradient(120deg, var(--photo-dark) 0%, #8a8a8a 45%, #d8d8d8 100%);
  }
  .front-backdrop {
    position: absolute; left: 290px; top: 0; right: 0; bottom: 0;
    background: linear-gradient(160deg, #d2d2d2 0%, #a9a9a9 100%);
  }
  .info-panel {
    position: absolute; left: 290px; top: 0; right: 0; bottom: 0;
    background: var(--panel);
    padding: 80px 26px 0 42px;
  }
  .info-panel__name {
    position: relative;
    font-family: "Josefin Slab", serif; font-weight: 600;
    font-size: 27px; line-height: 1.1; letter-spacing: 1px; color: var(--ink); text-transform: uppercase;
    white-space: nowrap;
  }
  .info-panel__name::before {
    content: ""; position: absolute; left: -18px; top: 2px;
    width: 7px; height: 24px; background: var(--pink);
  }
  .info-panel__role {
    font-family: "Josefin Slab", serif; font-weight: 600;
    font-size: 18px; color: var(--ink); text-align: right;
    margin-top: 4px; white-space: nowrap;
  }
  .contact-list { list-style: none; margin-top: 26px; }
  .contact-list__item {
    display: flex; align-items: center; gap: 14px;
    font-size: 16px; color: var(--ink); margin-bottom: 14px;
    white-space: nowrap;
  }
  .contact-list__icon { width: 22px; height: 22px; flex: none; }
</style>
</head>
<body>

  <section class="card card--back" aria-label="Card back">
    <div class="back-photo" role="img" aria-label="Teal-toned portrait photograph of Loretta Vanmeer"></div>
    <div class="title-band">
      <span class="title-band__kicker">Transformational</span>
      <h1 class="title-band__headline">LIFE COACH</h1>
      <div class="tagline-band">Growth &amp; Balance for Your Mind and Soul</div>
    </div>
  </section>

  <section class="card card--front" aria-label="Card front">
    <div class="front-photo" role="img" aria-label="Black and white portrait photograph of Loretta Vanmeer"></div>
    <div class="front-backdrop" role="img" aria-label="Faded grey continuation of the portrait"></div>
    <div class="info-panel">
      <h2 class="info-panel__name">Loretta Vanmeer</h2>
      <p class="info-panel__role">Transformational Life Coach</p>
      <ul class="contact-list">
        <li class="contact-list__item">
          <svg class="contact-list__icon" viewBox="0 0 24 24" aria-hidden="true"><path fill="#e6248f" d="M6.6 10.8a15 15 0 0 0 6.6 6.6l2.2-2.2c.3-.3.7-.4 1-.2 1.1.4 2.3.6 3.6.6.6 0 1 .4 1 1V20c0 .6-.4 1-1 1A17 17 0 0 1 3 4c0-.6.4-1 1-1h3.5c.6 0 1 .4 1 1 0 1.3.2 2.5.6 3.6.1.3 0 .7-.2 1z"/></svg>
          <span>555-318-4072</span>
        </li>
        <li class="contact-list__item">
          <svg class="contact-list__icon" viewBox="0 0 24 24" aria-hidden="true"><rect x="2" y="5" width="20" height="14" fill="#e6248f"/><path d="M2 5l10 8 10-8" fill="none" stroke="#fff" stroke-width="1.6"/></svg>
          <span>loretta@lorettavanmeer.example</span>
        </li>
        <li class="contact-list__item">
          <svg class="contact-list__icon" viewBox="0 0 24 24" aria-hidden="true"><circle cx="12" cy="12" r="10" fill="#e6248f"/><g fill="none" stroke="#fff" stroke-width="1.3"><ellipse cx="12" cy="12" rx="4.5" ry="10"/><path d="M2 12h20M4 7h16M4 17h16"/></g></svg>
          <span>www.lorettavanmeer.example</span>
        </li>
      </ul>
    </div>
  </section>

</body>
</html>
```